Business Card Design Project

Basketball Training program

Offers: Travel Club Program - Camps - Clinics - Private Training

website: ridgeportcourt.net
Phone Contact: Main Phone: 555-314-7720
Email: ridgeport.court@mailzone.example

Industry/Entity Type

Business

Contact Information for Business Card

Need one for the following coaches:
Marcus Thorne - Boys & Girls Basketball Coach
Kirasol Vendry - Girls Basketball Coach
Anselmo Trujar - Director/Head Coach
Walter Fisk- Boys Basketball
Howard Lindqvist - Boys Basketball
Ramon Etxeberri - Boys Basketball
Talvin Okafor- Boys Basketball/ Trainer
Al Hargrove - Boys & Girls Basketball Coach

Basketball Training program Logo - one side

Logo on the corner
new one on the left (RC)
old one on the right (old one is with the ridgeport and court)

```html
<!DOCTYPE html>
<html lang="en">
<head>
<meta charset="utf-8">
<title>Ridgeport Court — Business Card</title>
<link href="https://fonts.googleapis.com/css2?family=Open+Sans:ital,wght@0,400;0,600;0,800;1,400&display=swap" rel="stylesheet">
<style>
  :root {
    --backdrop: #3b3b3b;
    --card-white: #fbfbfb;
    --brand-yellow: #f8b100;
    --ink: #231f20;
    --ink-soft: #555555;
    --ink-mid: #333333;
  }
  * { box-sizing: border-box; margin: 0; padding: 0; }
  html, body { width: 1200px; height: 750px; overflow: hidden; }
  body {
    background: var(--backdrop);
    font-family: "Open Sans", Arial, sans-serif;
    position: relative;
  }
  .card {
    position: absolute;
    top: 228px;
    width: 461px;
    height: 263px;
    overflow: hidden;
  }
  .card-front { left: 124px; background: var(--card-white); }
  .card-back { left: 618px; background: var(--brand-yellow); }

  .monogram {
    position: absolute; left: 24px; top: 40px;
    display: flex; align-items: center; gap: 8px;
  }
  .monogram-dot { width: 14px; height: 14px; border-radius: 50%; background: var(--ink); }
  .monogram-name { font-weight: 800; font-size: 44px; color: var(--ink); line-height: 1; }

  .brand-mark {
    position: absolute; right: 22px; top: 48px;
    display: flex; align-items: center; gap: 7px;
  }
  .brand-dot { width: 16px; height: 16px; border-radius: 50%; background: var(--brand-yellow); }
  .brand-name { font-weight: 800; font-size: 19px; color: var(--ink); line-height: 1.05; text-align: left; }

  .name-tab {
    position: absolute; left: -11px; top: 142px;
    width: 22px; height: 35px; border-radius: 50%;
    background: var(--brand-yellow);
  }
  .coach-name {
    position: absolute; left: 22px; top: 137px;
    font-size: 18px; font-weight: 400; color: var(--brand-yellow); line-height: 1.2;
  }
  .coach-role {
    position: absolute; left: 22px; top: 159px;
    font-size: 13px; color: var(--ink); line-height: 1.3;
  }
  .role-rule {
    position: absolute; left: 200px; right: 21px; top: 168px;
    height: 1px; background: var(--brand-yellow);
  }
  .contact-list {
    position: absolute; left: 24px; top: 187px;
    list-style: none; font-size: 12px; color: var(--ink-soft);
  }
  .contact-list li { display: flex; align-items: center; gap: 6px; height: 17.5px; }
  .contact-list svg { width: 12px; height: 12px; fill: var(--brand-yellow); }

  .offers {
    position: absolute; right: 24px; top: 188px; text-align: right;
  }
  .offers-title { font-size: 14.5px; color: var(--brand-yellow); line-height: 1.2; }
  .offers-list { font-size: 12.5px; font-style: italic; color: var(--ink); line-height: 16px; }
  .bullet { color: var(--brand-yellow); font-style: normal; font-size: 9px; margin: 0 3px; vertical-align: 1px; }

  .base-rule { position: absolute; left: 0; right: 0; top: 254px; height: 1.5px; background: var(--ink-mid); }
  .base-band { position: absolute; left: 0; right: 0; top: 256px; height: 7px; background: var(--brand-yellow); }

  .back-mark {
    position: absolute; left: 0; right: 0; top: 0; bottom: 0;
    display: flex; align-items: center; justify-content: center; gap: 12px;
  }
  .back-dot { width: 26px; height: 26px; border-radius: 50%; background: var(--ink); }
  .back-name { font-weight: 800; font-size: 32px; color: var(--ink); line-height: 1.05; }
</style>
</head>
<body>
  <section class="card card-front">
    <div class="monogram"><span class="monogram-dot"></span><span class="monogram-name">RC</span></div>
    <div class="brand-mark"><span class="brand-dot"></span><span class="brand-name">Ridgeport<br>Court</span></div>

    <span class="name-tab"></span>
    <h1 class="coach-name">Marcus Thorne</h1>
    <p class="coach-role">Boys &amp; Girls Basketball Coach</p>
    <span class="role-rule"></span>

    <ul class="contact-list">
      <li><svg viewBox="0 0 24 24"><path d="M6.6 10.8a15.2 15.2 0 0 0 6.6 6.6l2.2-2.2a1 1 0 0 1 1-.25 11.4 11.4 0 0 0 3.6.57 1 1 0 0 1 1 1V20a1 1 0 0 1-1 1A17 17 0 0 1 3 4a1 1 0 0 1 1-1h3.5a1 1 0 0 1 1 1c0 1.25.2 2.45.57 3.6a1 1 0 0 1-.25 1z"/></svg>555-314-7720</li>
      <li><svg viewBox="0 0 24 24"><path d="M2 5h20v14H2z M2 5l10 8 10-8" /></svg>ridgeport.court@mailzone.example</li>
      <li><svg viewBox="0 0 24 24"><circle cx="12" cy="12" r="10"/></svg>ridgeportcourt.net</li>
    </ul>

    <div class="offers">
      <p class="offers-title">Offers:</p>
      <p class="offers-list">Travel Club Program<span class="bullet">●</span>Camps<br>Clinics<span class="bullet">●</span>Private Training</p>
    </div>

    <span class="base-rule"></span>
    <span class="base-band"></span>
  </section>

  <section class="card card-back">
    <div class="back-mark"><span class="back-dot"></span><span class="back-name">Ridgeport<br>Court</span></div>
  </section>
</body>
</html>
```